Chiropractic office needs updated web site

take the information/content from my existing website and redesign it to be more efficient and modern looking. i have a logo already designed that i have provided the files for. my office sees primarily athletes and their families and is geared toward active, healthy people who have sports injuries.
Updates

i originally started the project in february 2019 but am now just able to post the project. i need a new deadline calculated from todays (6-9-19) date.

Target Market(s)

injured athletes looking for a specific type of chiropractor.

Industry/Entity Type

Health Care

Contact Information for Business Card

I have a logo already designed and will provide that to all designers!

Coding

Coded - Design and coding required

Number of Pages Required

1 page

Font styles to use
Sans Serif

Colors

Designer to choose colors to be used in the design.

Requirements
Must have
• the current information/content already contained in my current website, belvanspinefit.com. i want this info redesigned and/or transferred to a new template. i will also provide new updated photos for use on the new site!
Nice to have
• modern, minimalist, creative looking website
Should not have
• typical medical website with boring, over-used stock photos of doctors, nurses and generic family types

```html
<!DOCTYPE html>
<html lang="en">
<head>
<meta charset="utf-8">
<title>Belvan Spinefit Chiropractic</title>
<link href="https://fonts.googleapis.com/css2?family=Montserrat:wght@500;600;700;800&family=Roboto:wght@400;500;700&display=swap" rel="stylesheet">
<style>
:root{
  --red:#e31b2b;
  --red-dark:#c8101e;
  --blue:#29a9e6;
  --blue-light:#44b8ee;
  --ink:#1d1d1f;
  --text:#555;
  --muted:#888;
  --nav:#333;
  --footer:#1e1e20;
  --line:#e3e3e3;
  --ghost:#ececec;
}
*{box-sizing:border-box;margin:0;padding:0}
html,body{width:1200px;height:4942px;overflow:hidden}
body{position:relative;background:#fff;font-family:Roboto,Arial,sans-serif;color:var(--text)}
.abs{position:absolute}
h1,h2,h3,.heading{font-family:Montserrat,Arial,sans-serif;color:var(--ink)}
.btn{position:absolute;display:flex;align-items:center;justify-content:center;gap:6px;border-radius:30px;font:700 14px Roboto,Arial,sans-serif;text-transform:uppercase}
.btn .dot{width:12px;height:12px;border-radius:50%;background:currentColor;display:inline-block;position:relative}
.btn-red{background:var(--red);color:#fff}
.btn-outline{border:2px solid var(--line);color:var(--red);background:#fff}
.ghost{position:absolute;font:800 92px Montserrat,Arial,sans-serif;color:var(--ghost);white-space:nowrap;letter-spacing:1px}
.section-title{position:absolute;left:0;width:1200px;text-align:center;font:800 40px Montserrat,Arial,sans-serif;color:var(--ink)}
.lede{position:absolute;left:190px;width:820px;text-align:center;font-size:14.5px;line-height:29px;color:var(--text)}

/* header */
.brand{left:112px;top:30px;display:flex;align-items:center;gap:12px}
.brand-mark{width:44px;height:44px;border-radius:50%;background:var(--red)}
.brand-name{font:700 24px Montserrat,Arial,sans-serif;color:var(--blue);line-height:1}
.brand-sub{font:500 9px Montserrat,Arial,sans-serif;color:var(--blue);letter-spacing:3px;margin-top:4px}
.contact-top{top:44px;left:500px;font-size:14.5px;color:#444;display:flex;gap:18px;align-items:center}
.contact-top svg{vertical-align:-2px;margin-right:6px}
.book{left:957px;top:34px;width:132px;height:42px;border-radius:22px;background:var(--red);color:#fff;font:700 13px Roboto,Arial,sans-serif;display:flex;align-items:center;justify-content:center}
.nav{left:0;top:104px;width:1200px;height:42px;background:var(--nav);display:flex;padding-left:158px;gap:28px;align-items:center}
.nav a{color:#fff;font:500 16px Roboto,Arial,sans-serif;text-decoration:none;text-transform:uppercase}

/* hero */
.hero-bg{left:0;top:146px;width:1200px;height:650px;background:linear-gradient(90deg,#f6f6f6 0%,#f2f2f2 45%,#e7e4e2 100%)}
.hero-photo{left:560px;top:146px;width:640px;height:630px;background:linear-gradient(135deg,#f3efec 0%,#e4d9d4 40%,#c9c2c4 70%,#8fa6b6 100%)}
.hero h1{position:absolute;left:112px;top:244px;font:800 37px Montserrat,Arial,sans-serif;color:var(--ink);letter-spacing:-.5px}
.hero .sub{position:absolute;left:112px;top:292px;font:600 29px Montserrat,Arial,sans-serif;color:var(--blue);letter-spacing:1px}
.area{position:absolute;display:flex;align-items:center;gap:14px;font:500 17px Roboto,Arial,sans-serif;color:#222}
.area i{width:46px;height:46px;border-radius:50%;background:var(--red);display:block;position:relative}
.area i::after{content:"";position:absolute;left:14px;top:14px;width:18px;height:18px;border:2px solid #fff;border-radius:50%}

/* about */
.about-portrait{left:102px;top:890px;width:430px;height:430px;border-radius:50%;background:radial-gradient(circle at 50% 40%,#8fc6f0 0%,#3fa9ec 55%,#2e8fd4 100%)}
.about-ring{left:92px;top:880px}
.about h2{position:absolute;left:584px;top:898px;font:800 40px Montserrat,Arial,sans-serif;color:var(--ink)}
.about .sub{position:absolute;left:584px;top:958px;font:600 20px Montserrat,Arial,sans-serif;color:var(--blue)}
.about p{position:absolute;left:584px;width:502px;font-size:13.5px;line-height:30px;color:#555;text-align:justify}

/* testimonials */
.testi{left:0;top:1542px;width:1200px;height:450px;background:linear-gradient(100deg,var(--red) 0%,#e41c2c 60%,#d4111f 100%)}
.testi .ghost{left:0;top:40px;color:rgba(255,255,255,.14);font-size:84px}
.testi h2{position:absolute;left:112px;top:86px;font:800 44px Montserrat,Arial,sans-serif;color:#fff;line-height:52px}
.testi p{position:absolute;left:112px;top:208px;width:430px;font-size:14.5px;line-height:30px;color:#fff}
.view{left:112px;top:306px;width:164px;height:46px;background:var(--blue);color:#fff}
.thumb{position:absolute;top:100px;height:250px}
.thumb-1{left:592px;width:416px;background:linear-gradient(180deg,#8fb1c9 0%,#6f8c5c 40%,#7a7a78 65%,#9a9692 100%)}
.thumb-2{left:1025px;width:175px;top:96px;height:258px;background:linear-gradient(180deg,#f2f2f2 0%,#d8c4b2 60%,#e7e7e7 100%);border:6px solid #fff}
.play{left:612px;top:290px;width:40px;height:40px;border-radius:50%;background:var(--blue)}
.next{left:999px;top:206px;width:40px;height:40px;border-radius:50%;background:#fff;border:2px solid var(--blue)}

/* treatments */
.card{position:absolute;top:2278px;width:294px;height:400px;background:#fff;box-shadow:0 4px 18px rgba(0,0,0,.12)}
.card .img{height:195px}
.card .icon{position:absolute;left:119px;top:164px;width:56px;height:56px;border-radius:50%;background:#fff;border:2px solid var(--blue)}
.card h3{position:absolute;top:234px;width:100%;text-align:center;font:600 21px Montserrat,Arial,sans-serif;color:#222}
.card p{position:absolute;top:280px;left:14px;right:14px;text-align:center;font-size:13.5px;line-height:26px;color:#666}
.card .btn{top:378px;left:84px;width:126px;height:38px;font-size:13.5px}

/* consultation */
.consult-title{top:2888px;color:#fff}
.consult-text{top:2960px;color:#fff}
.start{left:503px;top:3050px;width:194px;height:48px}

/* partners */
.partner{position:absolute;top:3476px;width:182px;height:92px;border:1px solid var(--line);background:#fff;display:flex;align-items:center;justify-content:center}
.partner span{display:block;width:110px;height:36px;border-radius:18px;background:#d9d9d9}
.divider{left:112px;top:3662px;width:976px;height:1px;background:var(--line)}

/* instagram */
.ig{position:absolute}

/* footer */
.footer{left:0;top:4490px;width:1200px;height:452px;background:var(--footer)}
.f-title{position:absolute;font:700 17px Montserrat,Arial,sans-serif;color:#fff;text-transform:uppercase}
.f-text{position:absolute;font-size:13.5px;line-height:26px;color:#ddd}
.field{position:absolute;height:42px;border:1px solid #666;color:#ccc;font-size:11px;padding:14px 12px}
.submit{left:333px;top:4716px;width:210px;height:42px;background:var(--red);color:#fff;font:700 15px Roboto,Arial,sans-serif;display:flex;align-items:center;justify-content:center;border-radius:2px}
.links{position:absolute;left:642px;top:4598px;list-style:none;font-size:13.5px;line-height:26px;color:#ddd}
.links li::before{content:"»";margin-right:22px;color:#aaa}
.cd{position:absolute;left:858px;display:flex;gap:20px;font-size:13.5px;line-height:24px;color:#ddd}
.cd i{width:32px;height:32px;border-radius:50%;border:1px solid #555;flex:none;display:block}
.social{position:absolute;top:4859px;width:36px;height:36px;border-radius:50%;border:2px solid #fff}
.copyright{position:absolute;left:0;top:4917px;width:1200px;text-align:center;font-size:14px;color:#fff}
</style>
</head>
<body>

<!-- HEADER -->
<div class="abs brand"><span class="brand-mark"></span><div><div class="brand-name">BELVAN SPINEFIT</div><div class="brand-sub">CHIROPRACTIC AND SPORTS THERAPY</div></div></div>
<div class="abs contact-top">
  <span><svg width="14" height="14" viewBox="0 0 24 24"><path fill="#29a9e6" d="M6.6 10.8a15 15 0 006.6 6.6l2.2-2.2a1 1 0 011-.25 11.4 11.4 0 003.6.57 1 1 0 011 1V20a1 1 0 01-1 1A17 17 0 013 4a1 1 0 011-1h3.5a1 1 0 011 1c0 1.25.2 2.45.57 3.57a1 1 0 01-.25 1z"/></svg>(+1) 123 456 7890</span>
  <span>|</span>
  <span><svg width="14" height="12" viewBox="0 0 24 20"><rect x="1" y="1" width="22" height="18" rx="2" fill="none" stroke="#29a9e6" stroke-width="2"/><path d="M1 3l11 8 11-8" fill="none" stroke="#29a9e6" stroke-width="2"/></svg>info@belvanspinefit.com</span>
</div>
<div class="abs book">BOOK NOW</div>
<nav class="abs nav"><a>Home</a><a>Location</a><a>Treatments</a><a>New Patient Paperwork</a><a>Stretching</a><a>Social</a><a>Gallery</a></nav>

<!-- HERO -->
<section class="hero">
  <div class="abs hero-bg"></div>
  <div class="abs hero-photo" role="img" aria-label="Woman stretching her knee on a yoga mat in a bright room"></div>
  <svg class="abs" style="left:0;top:680px" width="1200" height="120" viewBox="0 0 1200 120"><path d="M0 40 Q600 150 1200 40 L1200 120 L0 120Z" fill="#fff"/><path d="M0 40 Q600 150 1200 40" fill="none" stroke="#29a9e6" stroke-width="7"/></svg>
  <h1>BELVAN SPINEFIT</h1>
  <div class="sub">SPORTS THERAPY</div>
  <div class="area" style="left:112px;top:362px"><i></i>Hamstrings</div>
  <div class="area" style="left:345px;top:362px"><i></i>Hip Flexor</div>
  <div class="area" style="left:112px;top:425px"><i></i>Piriformis</div>
  <div class="area" style="left:345px;top:425px"><i></i>Pectorals</div>
  <div class="area" style="left:112px;top:487px"><i></i>Groin/Adductor</div>
  <div class="area" style="left:345px;top:487px"><i></i>Calves/Achilles</div>
  <div class="area" style="left:112px;top:550px"><i></i>Quadriceps</div>
  <div class="area" style="left:345px;top:550px"><i></i>Shin</div>
</section>

<!-- ABOUT -->
<section class="about">
  <div class="ghost" style="left:388px;top:850px">ABOUT BELVAN</div>
  <svg class="abs about-ring" width="450" height="450" viewBox="0 0 450 450"><path d="M225 10 A215 215 0 0 0 40 320" fill="none" stroke="#e31b2b" stroke-width="12"/><path d="M350 60 A215 215 0 0 1 410 330" fill="none" stroke="#e31b2b" stroke-width="4"/></svg>
  <div class="abs about-portrait" role="img" aria-label="Portrait of the clinic director in a blue shirt"></div>
  <h2>ABOUT BELVAN</h2>
  <div class="sub">I Am Dr. Wade Belvan</div>
  <p style="top:1016px">Dr. Wade Belvan is the owner and clinic director for Belvan Spinefit Chiropractic and Sports Therapy. He is a native Texan, growing up in the Dallas area and attended Northfield State University on a basketball scholarship.</p>
  <p style="top:1132px">Upon finishing his academic and basketball career at NSU, Dr. Belvan traveled and worked throughout Europe for 3 years before discovering beach volleyball and relocating to Miami Beach, FL. It was while competing on the East Coast pro-beach volleyball circuit that he experienced the awesome power of chiropractic and physical medicine. The injuries and chronic conditions that are a part of playing competitive sports had become debilitating...</p>
  <div class="btn btn-outline" style="left:584px;top:1380px;width:186px;height:48px">Read More <span class="dot"></span></div>
</section>

<!-- TESTIMONIALS -->
<section class="abs testi">
  <div class="ghost">CUSTOMER SAY</div>
  <h2>WHAT OUR<br>CUSTOMER SAY</h2>
  <p>Hear what our patients have to say in their own words; click a thumbnail below to load the testimonial video.</p>
  <div class="btn view">View All <span class="dot"></span></div>
  <div class="thumb thumb-1" role="img" aria-label="Runner sitting on a road holding her ankle"></div>
  <div class="thumb thumb-2" role="img" aria-label="Athlete sitting on the floor after training"></div>
  <div class="abs play" style="top:290px;left:612px"><svg width="40" height="40"><path d="M16 12l12 8-12 8z" fill="#fff"/></svg></div>
  <div class="abs next" style="top:206px;left:999px"><svg width="36" height="36"><path d="M15 11l7 7-7 7" fill="none" stroke="#29a9e6" stroke-width="3"/></svg></div>
</section>

<!-- TREATMENTS -->
<section>
  <div class="ghost" style="left:218px;top:2062px">OUR TREATMENTS</div>
  <div class="section-title" style="top:2106px">OUR TREATMENTS</div>
  <div class="lede" style="top:2182px">Lorem ipsum dolor sit amet, consectetur adipiscing elit, sed do eiusmod tempor incididunt ut labore et dolore magna aliqua. Ut enim ad minim veniam, quis nostrud exercitation ullamco laboris nisi ut.</div>

  <div class="card" style="left:112px">
    <div class="img" role="img" aria-label="Therapist treating a patient's back" style="background:linear-gradient(135deg,#e9e9e9,#b89c8a 55%,#d8d8d8)"></div>
    <div class="icon"></div>
    <h3>Belvan Protocol</h3>
    <p>The Belvan Protocol, or BP, is a comprehensive system of chiropractic and soft tissue therapy developed</p>
    <div class="btn btn-outline">Read More <span class="dot"></span></div>
  </div>
  <div class="card" style="left:452px">
    <div class="img" role="img" aria-label="Doctor examining an athlete's neck" style="background:linear-gradient(135deg,#f0f0f0,#c9b4a6 50%,#3f6f9c)"></div>
    <div class="icon"></div>
    <h3>Myofascial Therapy</h3>
    <p>Myofascial therapy is a safe, low force therapy that releases and heals soft tissue restrictions and tightness</p>
    <div class="btn btn-red">Read More <span class="dot"></span></div>
  </div>
  <div class="card" style="left:792px">
    <div class="img" role="img" aria-label="Athlete holding her lower back in a gym" style="background:linear-gradient(135deg,#5a5a5a,#cfcfcf 50%,#b98f7a)"></div>
    <div class="icon"></div>
    <h3>Trigger Point</h3>
    <p>Trigger point therapy addresses most muscle pains, which can occur at various points in the body</p>
    <div class="btn btn-outline">Read More <span class="dot"></span></div>
  </div>
</section>

<!-- CONSULTATION -->
<svg class="abs" style="left:0;top:2802px" width="1200" height="340" viewBox="0 0 1200 340"><defs><linearGradient id="cg" x1="0" x2="1"><stop offset="0" stop-color="#29a9e6"/><stop offset="1" stop-color="#3db5ee"/></linearGradient></defs><path d="M0 0H1200V280Q600 390 0 280Z" fill="url(#cg)"/></svg>
<h2 class="section-title consult-title" style="color:#fff">GET A FREE CONSULTATION</h2>
<div class="lede consult-text">Lorem ipsum dolor sit amet, consectetur adipiscing elit, sed do eiusmod tempor incididunt ut labore et dolore magna aliqua. Quis ipsum suspendisse ultrices gravida. Risus commodo viverra.</div>
<div class="btn btn-red start">Get Started <span class="dot"></span></div>

<!-- PARTNERS -->
<section>
  <div class="ghost" style="left:280px;top:3268px">OUR PARTNERS</div>
  <div class="section-title" style="top:3312px">OUR PARTNERS</div>
  <div class="lede" style="top:3386px;left:240px;width:720px">Lorem ipsum dolor sit amet, consectetur adipiscing elit, sed do eiusmod tempor incididunt ut labore et dolore magna aliqua. Ut enim ad minim veniam, quis nostrud exercitation ullamco laboris.</div>
  <div class="partner" style="left:112px"><span></span></div>
  <div class="partner" style="left:311px"><span></span></div>
  <div class="partner" style="left:510px"><span></span></div>
  <div class="partner" style="left:709px"><span></span></div>
  <div class="partner" style="left:907px"><span></span></div>
  <div class="abs divider"></div>
</section>

<!-- INSTAGRAM -->
<section>
  <div class="ghost" style="left:345px;top:3716px">INSTAGRAM</div>
  <div class="section-title" style="top:3760px">INSTAGRAM</div>
  <div class="ig" style="left:112px;top:3860px;width:258px;height:208px;background:linear-gradient(135deg,#2e3f6e,#8a8f9a 60%,#c7c7c7)" role="img" aria-label="Runner tying a shoe"></div>
  <div class="ig" style="left:112px;top:4076px;width:258px;height:208px;background:linear-gradient(135deg,#d9d4cf,#9c7e6c 50%,#c2c2c2)" role="img" aria-label="Group doing push-ups outdoors"></div>
  <div class="ig" style="left:378px;top:3860px;width:260px;height:424px;background:linear-gradient(160deg,#6c8a4a,#3d5a2c 45%,#b58b7a 75%,#e2c7bb)" role="img" aria-label="Trainer helping a woman with a knee injury on a trail"></div>
  <div class="ig" style="left:646px;top:3860px;width:442px;height:208px;background:var(--red);color:#fff;font:500 17px Roboto,Arial,sans-serif;display:flex;align-items:center;justify-content:center;gap:22px">
    <span>&#9679; 155</span><span>&#9829; 15K</span>
  </div>
  <div class="ig" style="left:646px;top:4076px;width:214px;height:208px;background:linear-gradient(160deg,#6f9a49,#3b6a2c 55%,#2f4c7a)" role="img" aria-label="Runner crouching on grass"></div>
  <div class="ig" style="left:870px;top:4076px;width:218px;height:208px;background:linear-gradient(160deg,#9dbb7d,#e8e8e8 50%,#5f8a3e)" role="img" aria-label="Soccer player being treated on the field"></div>
</section>

<!-- FOOTER -->
<svg class="abs" style="left:0;top:4380px" width="1200" height="120" viewBox="0 0 1200 120"><path d="M0 110 Q600 -20 1200 110 L1200 120 L0 120Z" fill="#1e1e20"/><path d="M60 100 Q600 -10 1140 100" fill="none" stroke="#29a9e6" stroke-width="6"/></svg>
<footer class="abs footer"></footer>
<div class="f-title" style="left:112px;top:4556px">Inquire Form</div>
<div class="f-text" style="left:112px;top:4594px;width:430px">At vero eos et accusamus et iusto odio dignissimos ducimus qui blanditiis praesentium voluptatum deleniti...</div>
<div class="field" style="left:112px;top:4660px;width:208px">Name</div>
<div class="field" style="left:333px;top:4660px;width:210px">Email</div>
<div class="field" style="left:112px;top:4716px;width:208px">Phone No</div>
<div class="abs submit">SUBMIT</div>

<div class="f-title" style="left:642px;top:4556px">Quick Links</div>
<ul class="links"><li>Home</li><li>About Us</li><li>Services</li><li>Locations</li><li>Treatments</li><li>Social</li><li>Contact Us</li></ul>

<div class="f-title" style="left:858px;top:4556px">Contact Details</div>
<div class="cd" style="top:4596px"><i></i><span>123A, Sample Street, Sample<br>City, New State.</span></div>
<div class="cd" style="top:4660px"><i></i><span style="line-height:32px">(+1) 123 456 7890</span></div>
<div class="cd" style="top:4720px"><i></i><span style="line-height:32px">info@belvanspinefit.com</span></div>

<div class="abs" style="left:112px;top:4877px;width:356px;height:1px;background:#555"></div>
<div class="abs" style="left:732px;top:4877px;width:356px;height:1px;background:#555"></div>
<div class="social" style="left:492px"></div>
<div class="social" style="left:536px"></div>
<div class="social" style="left:581px"></div>
<div class="social" style="left:626px"></div>
<div class="social" style="left:672px"></div>
<div class="copyright">Copyrights © 2019 Belvan Spinefit Chiropractic.&nbsp; All Rights Reserved &nbsp; | &nbsp; Privacy Policy.</div>

</body>
</html>
```